Electrician Company Website Design

I am looking to get a website designed only. I do not need it converted ot html. I simply need the design in a psd format. I have my own team for the conversion. The website is for an electrician company called Bramblecourt electric. I have created a txt document with the project parameters and specifics. I have also uploaded their logo in all avaible formats. It's a zip file.

Number of Pages Required

1 page

```html
<!DOCTYPE html>
<html lang="en">
<head>
<meta charset="utf-8">
<title>Bramblecourt Electric</title>
<link href="https://fonts.googleapis.com/css2?family=Raleway:wght@400;500;600&family=Varela+Round&display=swap" rel="stylesheet">
<style>
  :root {
    --red: #9b2024;
    --blue: #0f6ab4;
    --ink: #111111;
    --text: #222222;
    --muted: #9a9a9a;
    --grey-block: #b3b3b3;
    --section-grey: #f0eff0;
    --card-white: #f8f8f8;
    --white: #ffffff;
  }
  * { box-sizing: border-box; margin: 0; padding: 0; }
  html, body { width: 1200px; height: 3125px; overflow: hidden; }
  body { position: relative; background: var(--white); font-family: 'Raleway', sans-serif; color: var(--text); }
  .abs { position: absolute; }
  .heading { font-family: 'Varela Round', sans-serif; font-weight: 400; color: var(--ink); }
  .center { text-align: center; }

  /* Hero */
  .hero { position: absolute; left: 0; top: 0; width: 1200px; height: 680px;
    background: linear-gradient(90deg, #d9d4cc 0%, #cec6bb 40%, #b59d85 62%, #a0866d 78%, #c7c0b6 100%); }
  .site-header { position: absolute; left: 0; top: 0; width: 1200px; height: 93px; background: rgba(235,233,230,0.82); }
  .brand { position: absolute; left: 175px; top: 26px; width: 150px; display: flex; align-items: center; gap: 8px;
    font-size: 16px; line-height: 19px; font-weight: 600; color: var(--ink); }
  .brand-dot { flex: none; width: 16px; height: 16px; border-radius: 50%; background: var(--red); }
  .nav a { position: absolute; top: 38px; font-size: 16px; font-weight: 500; color: var(--ink); text-decoration: none; }
  .contact-btn { position: absolute; left: 917px; top: 29px; width: 108px; height: 35px; background: var(--red);
    color: var(--white); border-radius: 4px; font-size: 15px; font-weight: 500; display: flex; align-items: center; justify-content: center; }
  .hero-title { left: 175px; top: 238px; font-size: 39px; }
  .hero-text { left: 175px; top: 300px; width: 395px; font-size: 16.5px; line-height: 22.5px; }
  .hero-btn { left: 175px; top: 430px; width: 108px; height: 35px; background: var(--ink); color: var(--white);
    border-radius: 4px; font-size: 15px; font-weight: 500; display: flex; align-items: center; justify-content: center; }

  .section-title { left: 0; width: 1200px; font-size: 39px; }
  .section-text { left: 160px; width: 880px; font-size: 16.5px; line-height: 22.5px; }

  /* Service area cards */
  .area-block { position: absolute; }
  .area-card { position: absolute; background: var(--white); box-shadow: 2px 4px 8px rgba(0,0,0,0.18);
    display: flex; flex-direction: column; align-items: center; }
  .area-name { font-family: 'Varela Round', sans-serif; font-size: 40px; line-height: 44px; text-align: center; color: var(--ink); margin-top: 8px; }
  .area-link { display: flex; align-items: center; gap: 8px; font-size: 16.5px; margin-top: 10px; }

  /* Services */
  .services-bg { left: 0; top: 1254px; width: 1200px; height: 823px; background: var(--section-grey); }
  .service-card { position: absolute; width: 290px; height: 245px; box-shadow: 3px 4px 6px rgba(0,0,0,0.18);
    display: flex; flex-direction: column; align-items: center; justify-content: center; }
  .service-card.light { background: var(--card-white); }
  .service-card.featured { background: var(--blue); }
  .service-icon { width: 66px; height: 66px; border-radius: 50%; background: var(--ink); display: flex; align-items: center; justify-content: center;
    box-shadow: 1px 3px 4px rgba(0,0,0,0.3); margin-bottom: 22px; }
  .service-name { font-size: 25px; line-height: 29px; font-weight: 500; text-align: center; color: var(--ink); }
  .featured .service-name { color: var(--white); }
  .photo { position: absolute; }

  /* Gallery */
  .gallery-title { font-family: 'Varela Round', sans-serif; font-size: 25px; color: var(--ink); }
  .gallery-text { font-size: 16px; line-height: 22.5px; }
</style>
</head>
<body>

<section class="hero" role="img" aria-label="Photo of a smiling electrician in a white hard hat and round glasses"></section>

<header class="site-header">
  <div class="brand"><span class="brand-dot"></span><span>Bramblecourt<br>electric</span></div>
  <nav class="nav">
    <a style="left:362px">Company</a>
    <a style="left:472px">Service Area</a>
    <a style="left:605px">Services</a>
    <a style="left:707px">Gallery</a>
    <a style="left:800px">FAQs</a>
  </nav>
  <div class="contact-btn">Contact Us</div>
</header>

<h1 class="abs heading hero-title">About Us</h1>
<p class="abs hero-text">Lorem ipsum dolor sit amet, consetetur sadipscing elitr, sed diam nonumy eirmod tempor invidunt ut labore et dolore magna aliquyam erat, sed diam voluptua. At vero eos et accusam et justo duo</p>
<div class="abs hero-btn">Learn More</div>

<!-- Service area -->
<h2 class="abs heading center section-title" style="top:738px">Service Area</h2>
<p class="abs center section-text" style="top:798px">Lorem ipsum dolor sit amet, consetetur sadipscing elitr, sed diam nonumy eirmod tempor invidunt ut labore et<br>dolore magna aliquyam erat, sed diam voluptua. At vero eos et accusam et justo duo dolores et ea rebum.</p>

<div class="area-block" style="left:249px;top:918px;width:286px;height:266px;background:var(--red);box-shadow:2px 4px 6px rgba(0,0,0,0.2)"></div>
<div class="area-card" style="left:178px;top:944px;width:332px;height:216px;padding-top:6px">
  <svg width="34" height="50" viewBox="0 0 34 50"><path d="M17 2C9 2 3 8 3 16c0 10 14 26 14 26s14-16 14-26C31 8 25 2 17 2z" fill="var(--red)"/><circle cx="17" cy="16" r="6" fill="#fff"/><ellipse cx="17" cy="47" rx="10" ry="2" fill="#ddd"/></svg>
  <div class="area-name">Central<br>Minnesota</div>
  <div class="area-link" style="color:var(--red)"><svg width="22" height="12" viewBox="0 0 22 12"><path d="M0 6h20M15 1l5 5-5 5" stroke="var(--red)" stroke-width="1.5" fill="none"/></svg>Learn more</div>
</div>

<div class="area-block" style="left:664px;top:918px;width:285px;height:266px;background:var(--grey-block)"></div>
<div class="area-card" style="left:688px;top:944px;width:335px;height:214px;padding-top:4px">
  <svg width="34" height="50" viewBox="0 0 34 50"><path d="M17 2C9 2 3 8 3 16c0 10 14 26 14 26s14-16 14-26C31 8 25 2 17 2z" fill="#b0b0b0"/><circle cx="17" cy="16" r="6" fill="#fff"/><ellipse cx="17" cy="47" rx="10" ry="2" fill="#e3e3e3"/></svg>
  <div class="area-name">Surrounding<br>Countries</div>
  <div class="area-link" style="color:var(--muted)"><svg width="22" height="12" viewBox="0 0 22 12"><path d="M0 6h20M15 1l5 5-5 5" stroke="var(--muted)" stroke-width="1.5" fill="none"/></svg>Learn more</div>
</div>

<!-- Services -->
<div class="abs services-bg"></div>
<h2 class="abs heading center section-title" style="top:1313px">Our Services</h2>
<p class="abs center section-text" style="top:1372px">Lorem ipsum dolor sit amet, consetetur sadipscing elitr, sed diam nonumy eirmod tempor invidunt ut labore et<br>dolore magna aliquyam erat, sed diam voluptua. At vero eos et accusam et justo duo dolores et ea rebum.</p>

<div class="service-card featured" style="left:92px;top:1493px">
  <div class="service-icon"><svg width="40" height="40" viewBox="0 0 40 40" fill="none" stroke="#fff" stroke-width="2"><circle cx="20" cy="20" r="7"/><path d="M21 15l-3 5h4l-3 5"/><path d="M6 6l8 8M34 6l-8 8M6 34l8-8M34 34l-8-8"/></svg></div>
  <div class="service-name">Commerical Electrical<br>Services</div>
</div>
<div class="photo" role="img" aria-label="Photo of an electrician in a yellow hard hat working on a panel" style="left:455px;top:1493px;width:290px;height:245px;background:linear-gradient(135deg,#8a8a86,#5b4b3f 55%,#c9a43b);box-shadow:3px 4px 6px rgba(0,0,0,0.18)"></div>
<div class="service-card light" style="left:818px;top:1493px">
  <div class="service-icon"><svg width="40" height="40" viewBox="0 0 40 40" fill="none" stroke="#fff" stroke-width="2"><path d="M8 18L20 8l12 10v14H8z"/><path d="M21 15l-4 7h5l-4 7"/></svg></div>
  <div class="service-name">Residential Electrical<br>Services</div>
</div>

<div class="photo" role="img" aria-label="Photo of a technician reading a tablet in a workshop" style="left:92px;top:1770px;width:290px;height:245px;background:linear-gradient(135deg,#d8d8d6,#6e6e6c 50%,#2a2a2c);box-shadow:3px 4px 6px rgba(0,0,0,0.18)"></div>
<div class="service-card light" style="left:455px;top:1770px">
  <div class="service-icon"><svg width="40" height="40" viewBox="0 0 40 40" fill="none" stroke="#fff" stroke-width="2"><path d="M12 16a8 8 0 0116 0z"/><rect x="11" y="16" width="18" height="3"/><circle cx="20" cy="24" r="4"/><path d="M10 36v-4a10 6 0 0120 0v4"/></svg></div>
  <div class="service-name">Industrial Electrical<br>Services</div>
</div>
<div class="photo" role="img" aria-label="Photo of an engineer standing in a factory hall" style="left:818px;top:1770px;width:290px;height:245px;background:linear-gradient(180deg,#c7ccd2,#9ea3a8 55%,#6f7378);box-shadow:3px 4px 6px rgba(0,0,0,0.18)"></div>

<!-- Gallery -->
<h2 class="abs heading center section-title" style="top:2153px">Explore Our Gallery</h2>
<p class="abs center" style="left:300px;width:600px;top:2211px;font-size:16.5px;line-height:22.5px">Lorem ipsum dolor sit amet, consetetur sadipscing elitr, sed diam<br>nonumy eirmod tempor invidunt ut labore et dolore magna</p>

<div class="photo" role="img" aria-label="Photo of three engineers at a laptop beside machinery" style="left:0;top:2330px;width:382px;height:255px;background:linear-gradient(135deg,#2e3134,#8d9196 45%,#c7ccd0)"></div>
<h3 class="abs gallery-title" style="left:438px;top:2362px">Gallery</h3>
<p class="abs gallery-text" style="left:438px;top:2404px;width:600px">Lorem ipsum dolor sit amet, consetetur sadipscing elitr, sed diam nonumy<br>eirmod tempor invidunt ut labore et dolore magna aliquyam erat, sed diam<br>voluptua. At vero eos et accusam et justo duo dolores et ea rebum. &nbsp;&nbsp;&nbsp; clita<br>kasd gubergren, no sea takimata sanctus est Lorem ipsum dolor sit amet.<br>Lorem ipsum dolor sit amet, consetetur sadipscing elitr, sed diam nonumy<br>eirmod tempor invidunt ut labore et dolore magna aliquyam erat, sed diam</p>

<div class="photo" role="img" aria-label="Photo of a technician working among cables" style="left:818px;top:2655px;width:382px;height:255px;background:linear-gradient(135deg,#4a5a3a,#6f6a5e 45%,#2f3b48)"></div>
<h3 class="abs gallery-title" style="left:162px;width:600px;text-align:right;top:2680px">Gallery</h3>
<p class="abs gallery-text" style="left:162px;top:2722px;width:600px;text-align:right">Lorem ipsum dolor sit amet, consetetur sadipscing elitr, sed diam nonumy<br>eirmod tempor invidunt ut labore et dolore magna aliquyam erat, sed<br>diam voluptua. At vero eos et accusam et justo duo dolores et ea rebum.<br>clita kasd gubergren, no sea takimata sanctus est Lorem ipsum dolor sit<br>amet. Lorem ipsum dolor sit amet, consetetur sadipscing elitr, sed diam<br>nonumy eirmod tempor invidunt ut labore et dolore magna aliquyam erat,</p>

<div class="photo" role="img" aria-label="Photo of a technician at computer screens" style="left:0;top:2980px;width:382px;height:145px;background:linear-gradient(135deg,#cfd3d6,#5e6468 45%,#b5673f)"></div>
<h3 class="abs gallery-title" style="left:438px;top:3011px">Gallery</h3>
<p class="abs gallery-text" style="left:438px;top:3053px;width:600px">Lorem ipsum dolor sit amet, consetetur sadipscing elitr, sed diam nonumy<br>eirmod tempor invidunt ut labore et dolore magna aliquyam erat, sed diam<br>voluptua. At vero eos et accusam et justo duo dolores et ea rebum. &nbsp;&nbsp;&nbsp; clita</p>

</body>
</html>
```